Author needs a new book, Kindle and Audiobook cover design

I updated and re-edited a book I wrote 25 years ago but now realize the title and design did not get the job done. I am seeking a book, Kindle and audiobook design that will make me stand out. The final design will pop while being sensitive to the nature of the subject. The title of the book is Quiet Lanterns. Subtitle: Ways to Notice and Step Away From Harmful Circles While Keeping Steady Belief by Dorian T. Wexcombe. I am wanting to get the attention of people who have been damaged by a church relationship that started well but ended badly.
Updates

The book title is: Quiet Lanterns. The Subtitle is: Ways To Notice and Step Away From Harmful Circles While Keeping Steady Belief. The dimension is 6x9 (150 pages) and I am the author: Dorian T. Wexcombe

Target Market(s)

People with a church experience; church leadership. Religious abuse victims.

Industry/Entity Type

Christian

Font styles to use
Serif

Colors

Designer to choose colors to be used in the design.

Requirements
Nice to have
• I am not married to the Serif font if another design works better.

```html
<!DOCTYPE html>
<html lang="en">
<head>
<meta charset="utf-8">
<title>Quiet Lanterns — Dorian T. Wexcombe</title>
<link rel="stylesheet" href="https://fonts.googleapis.com/css2?family=Cinzel:wght@400&family=Tenor+Sans&family=Montserrat:wght@500&display=swap">
<style>
  :root {
    --paper: #ffffff;
    --title-grey: #9d9ea1;
    --author-grey: #6f7073;
    --subtitle-red: #e3000f;
    --sign-red: #c30b1b;
    --sky-top: #4c69bd;
    --sky-bottom: #93bdf5;
  }
  html, body {
    margin: 0;
    padding: 0;
    overflow: hidden;
    background: var(--paper);
  }
  .cover {
    position: relative;
    width: 802px;
    height: 1200px;
    background: var(--paper);
    overflow: hidden;
  }
  .title {
    position: absolute;
    left: 0;
    top: 52px;
    width: 100%;
    margin: 0;
    text-align: center;
    font-family: "Cinzel", "Times New Roman", serif;
    font-weight: 400;
    color: var(--title-grey);
    line-height: 112px;
  }
  .title-line {
    display: block;
    white-space: nowrap;
  }
  .title-line--first { font-size: 122px; }
  .title-line--second { font-size: 106px; }
  .subtitle {
    position: absolute;
    left: 0;
    top: 322px;
    width: 100%;
    margin: 0;
    text-align: center;
    font-family: "Tenor Sans", "Optima", sans-serif;
    font-weight: 400;
    font-size: 28px;
    line-height: 38px;
    color: var(--subtitle-red);
  }
  .subtitle-line {
    display: block;
    white-space: nowrap;
  }
  .prohibition {
    position: absolute;
    left: 0;
    top: 0;
    width: 802px;
    height: 1200px;
  }
  .author {
    position: absolute;
    left: 0;
    top: 1126px;
    width: 100%;
    margin: 0;
    text-align: center;
    font-family: "Montserrat", "Helvetica", sans-serif;
    font-weight: 500;
    font-size: 34px;
    letter-spacing: 0.16em;
    color: var(--author-grey);
    white-space: nowrap;
  }
</style>
</head>
<body>
  <main class="cover">
    <h1 class="title">
      <span class="title-line title-line--first">QUIET</span>
      <span class="title-line title-line--second">LANTERNS</span>
    </h1>

    <p class="subtitle">
      <span class="subtitle-line">Ways to NOTICE and STEP AWAY from HARMFUL</span>
      <span class="subtitle-line">CIRCLES WHILE KEEPING STEADY BELIEF</span>
    </p>

    <svg class="prohibition" viewBox="0 0 802 1200" xmlns="http://www.w3.org/2000/svg">
      <defs>
        <linearGradient id="sky" x1="0" y1="0" x2="0" y2="1">
          <stop offset="0" stop-color="var(--sky-top)"/>
          <stop offset="1" stop-color="var(--sky-bottom)"/>
        </linearGradient>
      </defs>
      <circle class="scene" cx="408" cy="750" r="260" fill="url(#sky)"
              role="img" aria-label="Photo of a white village church with a green steeple and clock under a clear blue sky, trees in front"/>
      <circle class="sign-ring" cx="408" cy="750" r="291" fill="none" stroke="var(--sign-red)" stroke-width="66"/>
      <rect class="sign-bar" x="108" y="719" width="600" height="62" fill="var(--sign-red)"
            transform="rotate(40 408 750)"/>
    </svg>

    <p class="author">DORIAN T. WEXCOMBE</p>
  </main>
</body>
</html>
```